Corvale Spine & Joint Business Card

Need a business card using the logo provided. I want brand side of the card to be grey with the logo in the center of the card in white.

On the other side I leave to the designers

Target Market(s)

Personal Injury Attorneys

Industry/Entity Type

Medical

Contact Information for Business Card

Name, CEO. Cell Phone, (Hialeah, Address, Phone) (Homestead, Address, Phone) (Tallahassee, Address, Phone)

Colors

Designer to choose only greyscale colors for use in the design.

Requirements
Must have
• Logo by itself on one side

```html
<!DOCTYPE html>
<html lang="en">
<head>
<meta charset="utf-8">
<title>Corvale Spine &amp; Joint – Business Card</title>
<link rel="stylesheet" href="https://fonts.googleapis.com/css2?family=Montserrat:ital,wght@0,400;0,500;0,600;1,400&display=swap">
<style>
  :root {
    --backdrop: #dcdcdc;
    --card-light: #f1f1f1;
    --card-light-edge: #e6e6e6;
    --brand: #8fa9b0;
    --brand-deep: #86a1a8;
    --ink: #1b1b1b;
    --swoosh-grey: #8a8a8a;
    --white: #ffffff;
  }
  * { margin: 0; padding: 0; box-sizing: border-box; }
  html, body {
    width: 1200px; height: 1164px; overflow: hidden;
    background: var(--backdrop);
    font-family: "Montserrat", Arial, sans-serif;
  }
  .stage {
    position: relative; width: 1200px; height: 1164px;
    display: flex; align-items: center; justify-content: center; gap: 24px;
  }
  .card {
    position: relative; width: 540px; height: 306px;
    border-radius: 16px; overflow: hidden;
    box-shadow: 0 2px 6px rgba(0,0,0,0.18);
  }
  .card-front {
    background: linear-gradient(180deg, var(--card-light) 0%, var(--card-light-edge) 100%);
    color: var(--ink);
  }
  .card-back { background: var(--brand); }

  .brand-name {
    font-weight: 500; text-transform: uppercase; text-align: center;
    line-height: 1;
  }
  .brand-name .primary { display: block; font-size: 40px; letter-spacing: 9px; }
  .brand-name .secondary { display: block; font-size: 17px; letter-spacing: 5px; margin-top: 8px; }
  .card-front .brand-name { position: absolute; top: 28px; right: 22px; color: var(--brand); }
  .card-back .brand-name {
    position: absolute; top: 50%; left: 50%; transform: translate(-50%, -50%);
    color: var(--white);
  }
  .card-back .brand-name .primary { font-size: 46px; letter-spacing: 10px; }
  .card-back .brand-name .secondary { font-size: 20px; letter-spacing: 6px; margin-top: 10px; }

  .person { position: absolute; left: 40px; top: 74px; }
  .person-name { font-size: 18px; font-weight: 500; letter-spacing: 0.3px; }
  .person-title { font-size: 11px; color: var(--brand); margin-top: 3px; }
  .contact-row { display: flex; align-items: center; gap: 5px; font-size: 13px; margin-top: 7px; }
  .contact-row:first-of-type { margin-top: 10px; }
  .contact-row svg { flex: none; }

  .locations { position: absolute; left: 40px; top: 183px; display: flex; }
  .location { font-size: 12.5px; line-height: 1.35; padding-right: 16px; }
  .location + .location { border-left: 1px solid #bcbcbc; padding-left: 18px; }
  .location-city { font-weight: 600; }
  .location-phone { display: flex; align-items: center; gap: 6px; margin-top: 4px; }

  .footer-band { position: absolute; left: 0; bottom: 0; width: 540px; height: 60px; }
  .website {
    position: absolute; right: 54px; bottom: 8px;
    font-size: 12.5px; font-style: italic; color: var(--white); letter-spacing: 0.3px;
  }
</style>
</head>
<body>
<main class="stage">
  <section class="card card-front" aria-label="Contact side">
    <div class="brand-name">
      <span class="primary">Corvale</span>
      <span class="secondary">Spine &amp; Joint</span>
    </div>

    <div class="person">
      <p class="person-name">DANIEL REYES</p>
      <p class="person-title">CEO</p>
      <p class="contact-row">
        <svg width="9" height="13" viewBox="0 0 9 13" aria-hidden="true"><rect x="1" y="0.5" width="7" height="12" rx="1.2" fill="none" stroke="#7d8f94" stroke-width="1"/><line x1="3.5" y1="10.5" x2="5.5" y2="10.5" stroke="#7d8f94"/></svg>
        555 0142 316
      </p>
      <p class="contact-row">
        <svg width="10" height="8" viewBox="0 0 10 8" aria-hidden="true"><rect x="0.5" y="0.5" width="9" height="7" fill="#8fa9b0"/><polyline points="0.5,0.5 5,4.5 9.5,0.5" fill="none" stroke="#fff" stroke-width="0.8"/></svg>
        info@corvale.com
      </p>
    </div>

    <div class="locations">
      <div class="location">
        <p class="location-city">Hialeah FL</p>
        <p>2280 Harbor Ave</p>
        <p>Hialeah, FL&nbsp; 4324</p>
        <p class="location-phone"><svg width="11" height="11" viewBox="0 0 11 11" aria-hidden="true"><path d="M2.2 1 L4 2.8 L3 4.2 Q4 6.5 6.8 8 L8.2 7 L10 8.8 L8.6 10.2 Q4.5 9.8 1 3.6 Z" fill="none" stroke="#7d8f94" stroke-width="0.9"/></svg>555 0142 316</p>
      </div>
      <div class="location">
        <p class="location-city">Homestead FL</p>
        <p>2280 Harbor Ave</p>
        <p>Homestead, FL&nbsp; 4324</p>
        <p class="location-phone"><svg width="11" height="11" viewBox="0 0 11 11" aria-hidden="true"><path d="M2.2 1 L4 2.8 L3 4.2 Q4 6.5 6.8 8 L8.2 7 L10 8.8 L8.6 10.2 Q4.5 9.8 1 3.6 Z" fill="none" stroke="#7d8f94" stroke-width="0.9"/></svg>555 0142 316</p>
      </div>
      <div class="location">
        <p class="location-city">Tallahassee FL</p>
        <p>2280 Harbor Ave</p>
        <p>Tallahassee, FL&nbsp; 4324</p>
        <p class="location-phone"><svg width="11" height="11" viewBox="0 0 11 11" aria-hidden="true"><path d="M2.2 1 L4 2.8 L3 4.2 Q4 6.5 6.8 8 L8.2 7 L10 8.8 L8.6 10.2 Q4.5 9.8 1 3.6 Z" fill="none" stroke="#7d8f94" stroke-width="0.9"/></svg>555 0142 316</p>
      </div>
    </div>

    <svg class="footer-band" viewBox="0 0 540 60" aria-hidden="true">
      <path d="M0 60 L0 56 Q200 12 400 10 Q200 20 110 60 Z" fill="var(--swoosh-grey)"/>
      <path d="M100 60 Q300 16 540 12 L540 60 Z" fill="var(--brand)"/>
    </svg>
    <p class="website">www.corvale.com</p>
  </section>

  <section class="card card-back" aria-label="Brand side">
    <div class="brand-name">
      <span class="primary">Corvale</span>
      <span class="secondary">Spine &amp; Joint</span>
    </div>
  </section>
</main>
</body>
</html>
```